The Plate Compass

Cutting Through the Noise to What Actually Works.

Nutrition book

Target Market(s)

People looking to be or get healthy and eat right.

```html
<!DOCTYPE html>
<html lang="en">
<head>
<meta charset="UTF-8">
<title>The Plate Compass – Book Cover</title>
<link href="https://fonts.googleapis.com/css2?family=Montserrat:wght@500;600;700;800&family=Passion+One:wght@700&display=swap" rel="stylesheet">
<style>
  :root {
    --paper: #fbfaf3;
    --ink: #1d2422;
    --forest: #0f4a3a;
    --forest-dark: #073328;
    --gold-light: #e7c36a;
    --gold: #c9a13f;
    --gold-dark: #a47d22;
    --rule: #c9a24a;
    --tag-supplements: #e6b21a;
    --tag-noise: #3c9f5a;
    --tag-timing: #16a7a3;
    --tag-quality: #1e9bd6;
    --tag-protein: #2a8ed9;
    --tag-calories: #4a7ed8;
  }
  * { margin: 0; padding: 0; box-sizing: border-box; }
  html, body { width: 800px; height: 1200px; overflow: hidden; background: var(--paper); }
  .cover {
    position: relative;
    width: 800px;
    height: 1200px;
    background: var(--paper);
    font-family: "Montserrat", Arial, sans-serif;
    overflow: hidden;
  }
  .backdrop-art {
    position: absolute;
    left: 20px; top: 300px;
    width: 760px; height: 720px;
    border-radius: 50%;
    background: radial-gradient(circle at 50% 50%,
      rgba(251,250,243,0) 0%,
      rgba(214,196,150,0.22) 30%,
      rgba(196,120,90,0.16) 48%,
      rgba(150,170,110,0.18) 62%,
      rgba(251,250,243,0) 72%);
  }
  .title {
    position: absolute;
    left: 0; right: 0; top: 50px;
    text-align: center;
    line-height: 1;
  }
  .title-the {
    display: block;
    font-family: "Montserrat", Arial, sans-serif;
    font-weight: 800;
    font-size: 64px;
    letter-spacing: 2px;
    color: var(--ink);
  }
  .title-main {
    display: block;
    margin-top: 4px;
    font-family: "Passion One", "Arial Black", sans-serif;
    font-weight: 700;
    font-size: 138px;
    letter-spacing: 2px;
    color: var(--forest);
    text-shadow: 0 3px 0 var(--forest-dark);
  }
  .title-sub {
    display: block;
    margin-top: -16px;
    font-family: "Passion One", "Arial Black", sans-serif;
    font-weight: 700;
    font-size: 104px;
    letter-spacing: 2px;
    background: linear-gradient(180deg, var(--gold-light) 0%, var(--gold) 55%, var(--gold-dark) 100%);
    -webkit-background-clip: text;
    background-clip: text;
    color: transparent;
  }
  .tagline {
    position: absolute;
    left: 0; right: 0; top: 372px;
    text-align: center;
    font-weight: 500;
    font-size: 25px;
    line-height: 35px;
    color: var(--ink);
  }
  .tagline-rule {
    position: absolute;
    top: 389px;
    width: 118px;
    height: 2px;
    background: var(--rule);
  }
  .tagline-rule.left { left: 66px; }
  .tagline-rule.right { left: 616px; }
  .pyramid { position: absolute; left: 0; top: 0; }
  .tier-label {
    font-family: "Montserrat", Arial, sans-serif;
    font-weight: 700;
    font-size: 18px;
    letter-spacing: 0.5px;
  }
  .author {
    position: absolute;
    left: 0; right: 0; top: 1118px;
    text-align: center;
    font-weight: 800;
    font-size: 26px;
    letter-spacing: 0.5px;
    color: var(--ink);
  }
  .base-band {
    position: absolute;
    left: 0; bottom: 0;
    width: 800px; height: 13px;
    background: linear-gradient(90deg, var(--gold-dark), var(--gold-light), var(--gold));
  }
</style>
</head>
<body>
<main class="cover">
  <div class="backdrop-art" role="img" aria-label="Faded circular arrangement of fruits, vegetables, grains, bubbles and fitness figures"></div>

  <h1 class="title">
    <span class="title-the">THE</span>
    <span class="title-main">PLATE</span>
    <span class="title-sub">COMPASS</span>
  </h1>

  <span class="tagline-rule left"></span>
  <p class="tagline">Cutting Through the Noise<br>to What Actually Works.</p>
  <span class="tagline-rule right"></span>

  <svg class="pyramid" width="800" height="1200" viewBox="0 0 800 1200" xmlns="http://www.w3.org/2000/svg">
    <defs>
      <linearGradient id="fill-supplements" x1="0" y1="0" x2="0" y2="1">
        <stop offset="0" stop-color="#f0c64a"/><stop offset="1" stop-color="#b9861c"/>
      </linearGradient>
      <linearGradient id="fill-noise" x1="0" y1="0" x2="1" y2="1">
        <stop offset="0" stop-color="#4f8a5c"/><stop offset="1" stop-color="#1f4f3a"/>
      </linearGradient>
      <linearGradient id="fill-timing" x1="0" y1="0" x2="1" y2="0">
        <stop offset="0" stop-color="#6fa58e"/><stop offset="0.5" stop-color="#c9c2a6"/><stop offset="1" stop-color="#4f8b6e"/>
      </linearGradient>
      <linearGradient id="fill-quality" x1="0" y1="0" x2="1" y2="0">
        <stop offset="0" stop-color="#3f7f92"/><stop offset="0.5" stop-color="#b65a4d"/><stop offset="1" stop-color="#4b8a7c"/>
      </linearGradient>
      <linearGradient id="fill-protein" x1="0" y1="0" x2="1" y2="0">
        <stop offset="0" stop-color="#7b8f93"/><stop offset="0.5" stop-color="#c4b59a"/><stop offset="1" stop-color="#6a7f86"/>
      </linearGradient>
      <linearGradient id="fill-calories" x1="0" y1="0" x2="1" y2="0">
        <stop offset="0" stop-color="#2c2f52"/><stop offset="0.35" stop-color="#9a6a4a"/><stop offset="0.65" stop-color="#b9a690"/><stop offset="1" stop-color="#c8a84a"/>
      </linearGradient>
    </defs>

    <polygon role="img" aria-label="Photo of golden supplement capsules" points="351,540 394,612 308,612" fill="url(#fill-supplements)"/>
    <polygon role="img" aria-label="Photo of tangled green cables" points="304,622 398,622 442,696 263,696" fill="url(#fill-noise)"/>
    <polygon role="img" aria-label="Photo of an alarm clock among plated meals" points="254,708 449,708 487,780 211,780" fill="url(#fill-timing)"/>
    <polygon role="img" aria-label="Photo of fresh vegetables and whole foods" points="204,794 493,794 536,866 163,866" fill="url(#fill-quality)"/>
    <polygon role="img" aria-label="Photo of eggs, nuts and other protein foods" points="156,880 540,880 584,952 114,952" fill="url(#fill-protein)"/>
    <polygon role="img" aria-label="Photo of beans, lentils, rice and corn" points="107,964 591,964 631,1037 68,1037" fill="url(#fill-calories)"/>

    <g class="tier supplements">
      <circle cx="398" cy="572" r="6" fill="none" stroke="var(--tag-supplements)" stroke-width="3"/>
      <text class="tier-label" x="420" y="579" fill="var(--tag-supplements)">SUPPLEMENTS</text>
    </g>
    <g class="tier noise">
      <circle cx="449" cy="656" r="6" fill="none" stroke="var(--tag-noise)" stroke-width="3"/>
      <text class="tier-label" x="470" y="663" fill="var(--tag-noise)">NOISE</text>
    </g>
    <g class="tier timing">
      <circle cx="493" cy="740" r="6" fill="none" stroke="var(--tag-timing)" stroke-width="3"/>
      <text class="tier-label" x="516" y="747" fill="var(--tag-timing)">MEAL TIMING</text>
    </g>
    <g class="tier quality">
      <circle cx="540" cy="825" r="6" fill="none" stroke="var(--tag-quality)" stroke-width="3"/>
      <text class="tier-label" x="563" y="832" fill="var(--tag-quality)">FOOD QUALITY</text>
    </g>
    <g class="tier protein">
      <circle cx="588" cy="911" r="6" fill="none" stroke="var(--tag-protein)" stroke-width="3"/>
      <text class="tier-label" x="616" y="918" fill="var(--tag-protein)">PROTEIN</text>
    </g>
    <g class="tier calories">
      <circle cx="636" cy="996" r="6" fill="none" stroke="var(--tag-calories)" stroke-width="3"/>
      <text class="tier-label" x="658" y="1003" fill="var(--tag-calories)">CALORIES</text>
    </g>
  </svg>

  <p class="author">DR. MORGAN ELLIS</p>
  <div class="base-band"></div>
</main>
</body>
</html>
```